Information Systems Internal Communication Brochure

We need a brochure that we can use as an internal marketing tool to highlight a number of the information technology projects we are working on across our business.

Looking for flat UI style design elements, needs to have four sections that cater for IT servers/storage/desktops, GIS (Mapping - Think Pelican Vista), Information Management and General Corporate Applications/Software.

Included in the files is the logo which needs to be incorporated into the design at the top right hand corner. Colours can also be used throughout if required.

The brochure needs to be easily editable by people with limited graphic design skills, and the graphics easily changeable to suit different projects.

```html
<!DOCTYPE html>
<html lang="en">
<head>
<meta charset="utf-8">
<title>Information Systems Brochure</title>
<link href="https://fonts.googleapis.com/css2?family=Source+Sans+3:wght@400;700&display=swap" rel="stylesheet">
<style>
  :root {
    --bg: #000000;
    --paper: #ffffff;
    --ink: #2b2b2b;
    --red: #c21f3a;
    --green: #8cc63f;
    --blue: #1f7cc4;
    --yellow: #f3d34a;
    --gold: #f0be2e;
    --brand: #2a6fb0;
  }
  * { box-sizing: border-box; margin: 0; padding: 0; }
  html, body { width: 899px; height: 1200px; overflow: hidden; background: var(--bg); }
  body { position: relative; font-family: "Source Sans 3", "Helvetica Neue", Arial, sans-serif; color: var(--ink); }

  .page { position: absolute; width: 405px; height: 575px; background: var(--paper); overflow: hidden; }
  .page--1 { left: 40px; top: 22px; }
  .page--2 { left: 463px; top: 22px; }
  .page--3 { left: 40px; top: 610px; }
  .page--4 { left: 463px; top: 610px; }

  .brand { position: absolute; right: 24px; top: 18px; display: flex; align-items: center; gap: 5px; color: var(--brand); font-weight: 700; }
  .brand__dot { width: 10px; height: 10px; border-radius: 50%; background: var(--brand); }
  .brand__name { font-size: 9px; line-height: 10px; text-align: center; text-transform: uppercase; letter-spacing: .5px; }

  .content { position: absolute; left: 47px; width: 303px; }
  .heading { font-size: 9.5px; font-weight: 700; text-transform: uppercase; line-height: 12px; margin-bottom: 9px; }
  .heading--red { color: var(--red); }
  .heading--green { color: var(--green); }
  .heading--blue { color: var(--blue); }
  .heading--gold { color: var(--gold); }
  .body-text { font-size: 8.5px; line-height: 11.4px; text-align: justify; margin-bottom: 11px; }
  .section { margin-top: 4px; }

  .callout { border-radius: 7px; padding: 6px 8px; margin-bottom: 9px; color: #fff; list-style: none; font-size: 8.5px; line-height: 11.4px; }
  .callout li::before { content: "•"; margin-right: 4px; }
  .callout--green { background: var(--green); }
  .callout--blue { background: var(--blue); }

  .photo { box-shadow: 2px 3px 5px rgba(0,0,0,.35); }
  .media-row { display: flex; gap: 18px; margin-top: 6px; }
  .media-row .photo { flex: 0 0 168px; height: 235px; background: linear-gradient(160deg, #f1f1f1 0%, #cfd3d8 40%, #2c2f36 100%); }
  .photo--wide { width: 300px; height: 216px; border-radius: 6px; background: linear-gradient(120deg, #d9d4cb 0%, #8a8f97 45%, #2a2c33 100%); margin-bottom: 20px; }

  .tab { position: absolute; right: 0; bottom: 0; width: 35px; height: 242px; border-radius: 8px 0 0 0; }
  .tab--red { background: var(--red); }
  .tab--green { background: var(--green); }
  .tab--blue { background: var(--blue); }
  .tab--yellow { background: var(--yellow); }
  .tab__label { position: absolute; left: 50%; top: 14px; transform-origin: 0 0; transform: rotate(90deg) translateY(-50%); white-space: nowrap; color: #fff; font-size: 10px; line-height: 12px; }

  .folio { position: absolute; left: 0; width: 100%; bottom: 6px; text-align: center; font-size: 8px; }
</style>
</head>
<body>

<section class="page page--1">
  <div class="brand"><span class="brand__dot"></span><span class="brand__name">Coralbay<br>Regional Council</span></div>
  <div class="content" style="top:76px">
    <h2 class="heading heading--red">Lorem ipsum dolor sit amet</h2>
    <p class="body-text">consectetur adipiscing elit. Aliquam tincidunt, nibh a pellentesque vestibulum, sem elit aliquam mi, eu dapibus elit nisi in mauris. In convallis ligula ut mauris hendrerit, ac mollis dolor porttitor. Quisque pulvinar sapien a mauris dictum, a eleifend urna tincidunt. Suspendisse pellentesque tincidunt nisl sit amet ultricies. Sed dictum nunc nisl, ut ultrices risus sollicitudin et. Praesent porttitor, ligula at lobortis rhoncus, dui diam placerat magna, at euismod mauris neque id lectus.</p>
    <h2 class="heading heading--red section">Mauris nec risus a sem sodales vulputate vitae in est.</h2>
    <p class="body-text">Aenean pulvinar risus eget metus luctus consequat consectetur non erat. Nulla quis dictum metus. Curabitur rutrum, augue sit amet sodales scelerisque, justo dui dignissim ligula, quis cursus arcu urna sed sapien. Curabitur ornare risus et egestas tristique. Curabitur vulputate, lectus sed mollis tincidunt, felis tellus posuere metus, quis varius velit sapien id odio.</p>
    <div class="media-row">
      <div class="photo" role="img" aria-label="Photo of two smiling colleagues working at a desktop computer"></div>
      <div>
        <p class="body-text">Ut pretium diam id aliquam auctor. Sed hendrerit dictum dapibus. Morbi hendrerit vestibulum libero, at venenatis ante pretium eu.</p>
        <p class="body-text">Phasellus viverra commodo augue, lobortis suscipit mi. In ullamcorper varius tellus, eget rutrum sapien interdum eget. Sed sed aliquam lacus, non malesuada magna.</p>
        <p class="body-text">Praesent semper nulla mi, eu aliquet tellus gravida vitae. Nunc accumsan id nisl ut condimentum. Aliquam vehicula enim non vestibulum tincidunt. Praesent sed semper tortor.</p>
      </div>
    </div>
  </div>
  <div class="tab tab--red"><span class="tab__label">IT servers/Storage/Desktops</span></div>
  <p class="folio">-1-</p>
</section>

<section class="page page--2">
  <div class="brand"><span class="brand__dot"></span><span class="brand__name">Coralbay<br>Regional Council</span></div>
  <div class="content" style="top:76px">
    <h2 class="heading heading--green">Donec nulla justo, sodales et ipsum non</h2>
    <p class="body-text">Ut pretium diam id aliquam auctor. Sed hendrerit dictum dapibus. Morbi hendrerit vestibulum libero, at venenatis ante pretium eu. Phasellus viverra commodo augue, lobortis suscipit mi. In ullamcorper varius tellus, eget rutrum sapien interdum eget. Sed sed aliquam lacus, non malesuada magna. Praesent semper nulla mi, eu aliquet tellus gravida vitae. Nunc accumsan id nisl ut condimentum. Aliquam vehicula enim non vestibulum tincidunt. Praesent sed semper tortor</p>
    <p class="body-text">Aenean pulvinar risus eget metus luctus consequat consectetur non erat. Nulla quis dictum metus. Curabitur rutrum, augue sit amet sodales scelerisque, justo dui dignissim ligula, quis cursus arcu urna sed sapien. Curabitur ornare risus et egestas tristique. Curabitur vulputate, lectus sed mollis tincidunt, felis tellus posuere metus, quis varius velit sapien id odio.</p>
    <ul class="callout callout--green">
      <li>Ut pretium diam id aliquam auctor. Sed hendrerit dictum dapibus.</li>
      <li>Morbi hendrerit vestibulum libero, at venenatis ante pretium eu.</li>
      <li>Phasellus viverra commodo augue, lobortis suscipit mi.</li>
      <li>In ullamcorper varius tellus, eget rutrum sapien interdum eget.</li>
      <li>Sed sed aliquam lacus, non malesuada magna.</li>
    </ul>
    <p class="body-text">Praesent semper nulla mi, eu aliquet tellus gravida vitae. Nunc accumsan id nisl ut condimentum. Aliquam vehicula enim non vestibulum tincidunt. Praesent sed semper tortor.</p>
    <h2 class="heading heading--green section">Nulla facilisis at risus sit amet fermentum.</h2>
    <p class="body-text">Suspendisse pellentesque tincidunt nisl sit amet ultricies. Sed dictum nunc nisl, ut ultrices risus sollicitudin et. Praesent porttitor, ligula at lobortis rhoncus, dui diam placerat magna, at euismod mauris neque id lectus. Vestibulum adipiscing odio quis rhoncus gravida. Mauris nec risus a sem sodales vulputate vitae in est. Aenean pulvinar risus eget metus luctus consequat consectetur non erat. Nulla quis dictum metus.</p>
    <p class="body-text">Mauris id lacinia est, vel volutpat quam. In sit amet erat nulla. Aenean venenatis rutrum orci eget ultricies. Fusce felis nunc, elementum eu leo et, tristique consectetur odio. Quisque mollis mi eu nibh blandit egestas. Donec sit amet lorem et sapien scelerisque consequat.</p>
  </div>
  <div class="tab tab--green"><span class="tab__label">GIS (Mapping - Think Pelican Vista)</span></div>
  <p class="folio">-2-</p>
</section>

<section class="page page--3">
  <div class="brand"><span class="brand__dot"></span><span class="brand__name">Coralbay<br>Regional Council</span></div>
  <div class="content" style="top:76px">
    <h2 class="heading heading--blue">Donec nulla justo, sodales et ipsum non</h2>
    <p class="body-text">Ut pretium diam id aliquam auctor. Sed hendrerit dictum dapibus. Morbi hendrerit vestibulum libero, at venenatis ante pretium eu. Phasellus viverra commodo augue, lobortis suscipit mi. In ullamcorper varius tellus, eget rutrum sapien interdum eget. Sed sed aliquam lacus, non malesuada magna. Praesent semper nulla mi, eu aliquet tellus gravida vitae. Nunc accumsan id nisl ut condimentum. Aliquam vehicula enim non vestibulum tincidunt. Praesent sed semper tortor</p>
    <p class="body-text">Aenean pulvinar risus eget metus luctus consequat consectetur non erat. Nulla quis dictum metus. Curabitur rutrum, augue sit amet sodales scelerisque, justo dui dignissim ligula, quis cursus arcu urna sed sapien. Curabitur ornare risus et egestas tristique. Curabitur vulputate, lectus sed mollis tincidunt, felis tellus posuere metus, quis varius velit sapien id odio.</p>
    <ul class="callout callout--blue">
      <li>Ut pretium diam id aliquam auctor. Sed hendrerit dictum dapibus.</li>
      <li>Morbi hendrerit vestibulum libero, at venenatis ante pretium eu.</li>
      <li>Phasellus viverra commodo augue, lobortis suscipit mi.</li>
      <li>In ullamcorper varius tellus, eget rutrum sapien interdum eget.</li>
      <li>Sed sed aliquam lacus, non malesuada magna.</li>
    </ul>
    <p class="body-text">Praesent semper nulla mi, eu aliquet tellus gravida vitae. Nunc accumsan id nisl ut condimentum. Aliquam vehicula enim non vestibulum tincidunt. Praesent sed semper tortor.</p>
    <h2 class="heading heading--blue section">Nulla facilisis at risus sit amet fermentum.</h2>
    <p class="body-text">Suspendisse pellentesque tincidunt nisl sit amet ultricies. Sed dictum nunc nisl, ut ultrices risus sollicitudin et. Praesent porttitor, ligula at lobortis rhoncus, dui diam placerat magna, at euismod mauris neque id lectus. Vestibulum adipiscing odio quis rhoncus gravida. Mauris nec risus a sem sodales vulputate vitae in est. Aenean pulvinar risus eget metus luctus consequat consectetur non erat. Nulla quis dictum metus.</p>
    <p class="body-text">Mauris id lacinia est, vel volutpat quam. In sit amet erat nulla. Aenean venenatis rutrum orci eget ultricies. Fusce felis nunc, elementum eu leo et, tristique consectetur odio. Quisque mollis mi eu nibh blandit egestas. Donec sit amet lorem et sapien scelerisque consequat.</p>
  </div>
  <div class="tab tab--blue"><span class="tab__label">Information Management</span></div>
  <p class="folio">-3-</p>
</section>

<section class="page page--4">
  <div class="brand"><span class="brand__dot"></span><span class="brand__name">Coralbay<br>Regional Council</span></div>
  <div class="content" style="top:77px">
    <div class="photo photo--wide" role="img" aria-label="Photo of two business colleagues reviewing a tablet together outdoors"></div>
    <h2 class="heading heading--gold">Lorem ipsum dolor sit amet</h2>
    <p class="body-text">consectetur adipiscing elit. Aliquam tincidunt, nibh a pellentesque vestibulum, sem elit aliquam mi, eu dapibus elit nisi in mauris. In convallis ligula ut mauris hendrerit, ac mollis dolor porttitor. Quisque pulvinar sapien a mauris dictum, a eleifend urna tincidunt. Suspendisse pellentesque tincidunt nisl sit amet ultricies. Sed dictum nunc nisl, ut ultrices risus sollicitudin et. Praesent porttitor, ligula at lobortis rhoncus, dui diam placerat magna, at euismod mauris neque id lectus.</p>
    <h2 class="heading heading--gold section">Mauris nec risus a sem sodales vulputate vitae in est.</h2>
    <p class="body-text">Aenean pulvinar risus eget metus luctus consequat consectetur non erat. Nulla quis dictum metus. Curabitur rutrum, augue sit amet sodales scelerisque, justo dui dignissim ligula, quis cursus arcu urna sed sapien. Curabitur ornare risus et egestas tristique. Curabitur vulputate, lectus sed mollis tincidunt, felis tellus posuere metus, quis varius velit sapien id odio.Ut pretium diam id aliquam auctor. Sed hendrerit dictum dapibus. Morbi hendrerit vestibulum libero, at venenatis ante pretium eu.</p>
  </div>
  <div class="tab tab--yellow"><span class="tab__label">General Corporate Applications/Software</span></div>
  <p class="folio">-4-</p>
</section>

</body>
</html>
```